Easy - Fix our "Snag the Bash" Promo Flyer

Please see attached promo flyer with all the information required. Looking for quick assistance so we can go live with the advertising for this competition. Looking for something more commercial and polished. Very attractive so that lots of people enter the competition. <br/><br/>Happy for it to look a little bit festive as the competition is running in December. <br/><br/>Attached is out Fork Lodge Logo and first attempts at poster. Please let me know if you need anything further. <br/><br/>If you see any grammar or spelling errors please feel free to fix too.
Target Market(s)
Corporate Businesses who are buying vouchers as staff christmas gifts/bonus
Colors
Designer to choose colors to be used in the design.
Look and feel

```html
<!DOCTYPE html>
<html lang="en">
<head>
<meta charset="utf-8">
<title>Snag the Bash – Staff Party Voucher Promo</title>
<link href="https://fonts.googleapis.com/css2?family=Itim&family=Yellowtail&display=swap" rel="stylesheet">
<style>
  :root {
    --page-bg: #2a2a2c;
    --flyer-top: #72757a;
    --flyer-mid: #3a3b3d;
    --flyer-bottom: #161617;
    --gold: #f0c23a;
    --gold-light: #ffe08a;
    --gold-deep: #b07a18;
    --white: #ffffff;
    --pine: #467f2f;
    --pine-dark: #2f5f22;
    --cone: #7a5232;
    --ribbon-text: #1c1c1c;
  }
  * { box-sizing: border-box; margin: 0; padding: 0; }
  html, body { width: 1200px; height: 1010px; overflow: hidden; }
  body { background: var(--page-bg); font-family: "Itim", sans-serif; position: relative; }

  .flyer {
    position: absolute; left: 283px; top: 57px; width: 634px; height: 896px;
    background: radial-gradient(ellipse at 50% 28%, var(--flyer-top) 0%, var(--flyer-mid) 48%, var(--flyer-bottom) 100%);
    box-shadow: 0 8px 30px rgba(0,0,0,.6);
    overflow: hidden; color: var(--gold);
  }
  .line { position: absolute; left: 0; width: 100%; text-align: center; white-space: nowrap; }

  .pine-branch {
    position: absolute; left: 172px; top: 37px; width: 289px; height: 255px;
    border-radius: 50%;
    background: radial-gradient(ellipse closest-side, var(--pine) 0%, var(--pine-dark) 50%, rgba(122,82,50,.75) 78%, rgba(122,82,50,0) 100%);
  }
  .sparkle { position: absolute; border-radius: 50%;
    background: radial-gradient(circle at 35% 35%, var(--gold-light), var(--gold-deep)); }

  .kicker { top: 289px; font-size: 27px; line-height: 34px; letter-spacing: 2px; }
  .headline {
    top: 320px; font-family: "Yellowtail", cursive; font-size: 112px; line-height: 130px; font-weight: 400;
    background: linear-gradient(90deg, var(--gold-deep), var(--gold-light) 45%, var(--gold) 70%, var(--gold-deep));
    -webkit-background-clip: text; background-clip: text; color: transparent;
  }
  .subhead { top: 441px; font-size: 27px; line-height: 34px; letter-spacing: 2px; }
  .offer { top: 497px; font-size: 19px; line-height: 26px; letter-spacing: 1.5px; }
  .ribbon { position: absolute; left: 219px; top: 523px; width: 196px; height: 26px; }
  .ribbon-text { top: 523px; font-size: 18px; line-height: 26px; color: var(--ribbon-text); letter-spacing: 1px; }
  .ribbon-text sup { font-size: 10px; }
  .draw { top: 548px; font-size: 19px; line-height: 26px; letter-spacing: 1.5px; }
  .rule { position: absolute; left: 105px; top: 603px; width: 424px; height: 1px; background: var(--gold); }

  .details { top: 618px; font-size: 12px; line-height: 16.5px; letter-spacing: .5px; }
  .tip { top: 686px; font-size: 12px; line-height: 16.5px; letter-spacing: .5px; }

  .contacts {
    position: absolute; top: 747px; left: 0; width: 100%; height: 22px;
    display: flex; justify-content: center; align-items: center; gap: 16px;
    font-size: 15px; letter-spacing: .8px;
  }
  .contact { display: flex; align-items: center; gap: 5px; }
  .dot { width: 9px; height: 9px; border-radius: 50%; background: var(--gold); }
  .social-mark { width: 10px; height: 10px; border-radius: 50%; border: 1.5px solid var(--gold); }

  .voucher { position: absolute; top: 785px; width: 146px; height: 50px; }
  .voucher-kraft { left: 86px; background: linear-gradient(90deg, #c9a77a, #e4cfa8); }
  .voucher-yellow { left: 244px; background: linear-gradient(90deg, #f6c900, #fff3c4 45%, #fff); }
  .voucher-red { left: 403px; background: linear-gradient(90deg, #d9232a, #f5f5f5 45%, #fff); }

  .brand {
    position: absolute; left: 552px; top: 782px; width: 70px;
    font-size: 20px; line-height: 24px; color: var(--white); text-align: center;
  }

  .footer { top: 850px; font-size: 13px; line-height: 17px; letter-spacing: 1px; color: var(--white); }
</style>
</head>
<body>
  <main class="flyer">
    <div class="pine-branch" role="img" aria-label="Illustrated pine branch with three pine cones"></div>

    <span class="sparkle" style="left:202px;top:62px;width:9px;height:9px"></span>
    <span class="sparkle" style="left:383px;top:70px;width:11px;height:11px"></span>
    <span class="sparkle" style="left:89px;top:162px;width:11px;height:11px"></span>
    <span class="sparkle" style="left:475px;top:188px;width:12px;height:12px"></span>
    <span class="sparkle" style="left:19px;top:284px;width:9px;height:9px"></span>
    <span class="sparkle" style="left:158px;top:294px;width:8px;height:8px"></span>
    <span class="sparkle" style="left:410px;top:329px;width:10px;height:10px"></span>
    <span class="sparkle" style="left:583px;top:437px;width:11px;height:11px"></span>
    <span class="sparkle" style="left:630px;top:527px;width:7px;height:7px"></span>
    <span class="sparkle" style="left:603px;top:565px;width:10px;height:10px"></span>
    <span class="sparkle" style="left:12px;top:699px;width:11px;height:11px"></span>
    <span class="sparkle" style="left:610px;top:890px;width:11px;height:11px"></span>

    <p class="line kicker">Win the ultimate</p>
    <h1 class="line headline">Staff Party</h1>
    <p class="line subhead">for you &amp; your colleagues</p>

    <p class="line offer">Purchase K5,000 worth of vouchers before</p>
    <svg class="ribbon" viewBox="0 0 196 26" aria-hidden="true">
      <defs>
        <linearGradient id="ribbonGold" x1="0" x2="1">
          <stop offset="0" stop-color="#b07a18"/>
          <stop offset=".5" stop-color="#ffe08a"/>
          <stop offset="1" stop-color="#b07a18"/>
        </linearGradient>
      </defs>
      <polygon points="0,0 196,0 184,13 196,26 0,26 12,13" fill="url(#ribbonGold)"/>
    </svg>
    <p class="line ribbon-text">December 31<sup>st</sup></p>

    <p class="line draw">and go into the draw to WIN<br>the ultimate staff party for 150 people.</p>
    <span class="rule"></span>

    <p class="line details">This includes a venue, BBQ-style PNG menu, roast pig, decor and much more…<br>So HURRY! There are ONLY 2 parties to WIN!<br>We'll even throw in an extra-large themed cake with your company logo on it.</p>

    <p class="line tip">TIP: Buy more vouchers for a better chance of winning.<br>"For every HR department enquiry we receive, a special surprise will be given,<br>so HURRY and contact us below on…"</p>

    <div class="contacts">
      <span class="contact">
        <svg width="17" height="17" viewBox="0 0 24 24" aria-hidden="true"><path d="M6.6 2.5l3 3.3-1.8 2.6c1.3 2.8 3.4 4.9 6.2 6.2l2.6-1.8 3.3 3-1.6 3.2C11 18.6 5.4 13 4.4 4.1z" fill="none" stroke="currentColor" stroke-width="1.6" stroke-linejoin="round"/></svg>
        7000 4521
      </span>
      <span class="dot"></span>
      <span class="contact">@ sales@forklodge.com.pg</span>
      <span class="dot"></span>
      <span class="contact"><span class="social-mark"></span>forklodgepng</span>
    </div>

    <div class="voucher voucher-kraft" role="img" aria-label="Kraft paper K100 shopping voucher sample"></div>
    <div class="voucher voucher-yellow" role="img" aria-label="Yellow K50 shopping voucher sample"></div>
    <div class="voucher voucher-red" role="img" aria-label="Red K100 shopping voucher sample"></div>
    <div class="brand">FORK<br>LODGE</div>

    <p class="line footer">Have a MERRY XMAS at FORK LODGE!<br>Terms and conditions apply</p>
  </main>
</body>
</html>
```